Pebble Brook Cafe Take Out Menu

We serve coffee and tea made from our very own reverse osmosis water. Serve sandwiches, soups, pastry and more. Christian company! Want a to go menu so it needs to be condensed from one I sent you.

Target Market(s)

Portales and Roosevelt County NM

Industry/Entity Type

Coffee Shop

```html
<!DOCTYPE html>
<html lang="en">
<head>
<meta charset="utf-8">
<title>Pebble Brook Cafe – Take Out Menu</title>
<link href="https://fonts.googleapis.com/css2?family=Courgette&family=Roboto+Condensed:wght@400;700&family=Playfair+Display:wght@700&display=swap" rel="stylesheet">
<style>
:root{
  --wood:#a9773f;
  --wood-dark:#7a5027;
  --paper:#fbf3de;
  --paper-edge:#e9d9b3;
  --rust:#9a2f17;
  --red:#c2271b;
  --green:#5c8c2b;
  --green-dark:#3f6a1a;
  --ink:#2e2218;
  --muted:#6b5a48;
  --gold:#f1cf5a;
  --photo-a:#c79a62;
  --photo-b:#8e6a3f;
}
*{box-sizing:border-box;margin:0;padding:0}
html,body{width:800px;height:1200px;overflow:hidden;background:var(--wood)}
body{font-family:"Roboto Condensed",Arial,sans-serif;color:var(--ink);position:relative}
.panel{position:absolute;left:0;width:800px;background:linear-gradient(90deg,var(--wood-dark),var(--wood) 20%,#b8874c 50%,var(--wood) 80%,var(--wood-dark))}
.panel--top{top:0;height:598px}
.panel--bottom{top:602px;height:598px}
.sheet{position:absolute;background:var(--paper);border:1px solid var(--paper-edge)}
.photo{position:absolute;background:linear-gradient(135deg,var(--photo-a),var(--photo-b));border-radius:3px}
.photo--round{border-radius:50%}
.script{font-family:"Courgette",cursive;color:var(--rust)}
.tab{position:absolute;background:var(--paper);text-align:center;font-size:22px;padding-top:4px;box-shadow:0 2px 4px rgba(0,0,0,.25)}
.head-tag{position:absolute;font-family:"Courgette",cursive;color:var(--rust);font-size:17px;background:var(--paper-edge);padding:2px 12px;border-radius:2px}
.item{position:absolute;font-size:10px;line-height:1.25;color:var(--muted)}
.item b{display:flex;justify-content:space-between;font-size:12px;color:var(--rust);text-transform:uppercase;letter-spacing:.2px}
.item b span{color:var(--ink)}
.price-badge{position:absolute;border-radius:50%;background:var(--green);color:#fff;font-weight:700;display:flex;align-items:center;justify-content:center;border:3px solid #fff}
.wraps-band{position:absolute;background:var(--green);color:#fff;font-family:"Courgette",cursive;font-size:20px;padding:2px 14px}
.wrap-text{position:absolute;font-size:11px;line-height:1.45}
.wrap-text strong{color:var(--rust)}
.extras{position:absolute;background:var(--gold);padding:6px 10px;font-size:10px;line-height:1.4}
.extras h4{font-family:"Courgette",cursive;color:var(--rust);font-size:16px;font-weight:400}
.fruit-tag{position:absolute;background:var(--red);color:#fff;font-family:"Courgette",cursive;font-size:13px;padding:3px 8px;border-radius:3px;text-align:center}
.sides-table{position:absolute;font-size:11px;border-collapse:collapse}
.sides-table th{text-align:left;color:var(--rust);font-weight:700;padding:2px 6px}
.sides-table td{padding:2px 6px}
.pastry{position:absolute;left:22px;width:210px;height:52px}
.pastry .photo{left:0;top:2px;width:44px;height:44px}
.pastry .item{left:52px;top:4px;width:158px}
.size-bar{position:absolute;background:var(--green);color:#fff;font-weight:700;font-size:13px;display:flex;justify-content:space-around;align-items:center}
.kids-pill{position:absolute;background:var(--green);color:#fff;font-family:"Courgette",cursive;font-size:16px;padding:2px 14px;border-radius:12px}
.kid-box{position:absolute;background:var(--green-dark);color:#fff;text-align:center;font-size:10px;padding:6px;line-height:1.3}
.kid-box b{display:block;font-size:12px}
.kid-box i{display:block;font-style:normal;font-size:15px;font-weight:700;margin-top:4px}
.note{position:absolute;background:var(--red);color:#fff;font-size:10px;text-align:center;padding:6px;line-height:1.35;font-weight:700}
.thanks{position:absolute;font-size:10px;text-align:center;color:var(--muted)}
.brand-card{position:absolute;background:#fff;border:1px solid var(--paper-edge)}
.ribbon{position:absolute;left:-12px;right:-12px;top:28px;height:30px;background:var(--ink);color:#fff;font-size:14px;font-weight:700;text-align:center;line-height:30px;letter-spacing:.5px}
.ribbon::before,.ribbon::after{content:"";position:absolute;top:4px;width:14px;height:22px;background:var(--red)}
.ribbon::before{left:-10px}.ribbon::after{right:-10px}
.icons{position:absolute;top:250px;left:0;right:0;display:flex;justify-content:center;gap:18px;font-size:10px;color:var(--muted);text-align:center}
.icons svg{display:block;margin:0 auto 3px}
.menu-word{position:absolute;top:300px;left:0;right:0;text-align:center;font-family:"Playfair Display",serif;font-size:44px;letter-spacing:4px;color:var(--ink)}
.menu-rule{position:absolute;top:296px;left:40px;right:40px;border-top:1px solid var(--ink)}
.menu-rule--low{top:360px}
</style>
</head>
<body>

<!-- TOP PANEL -->
<section class="panel panel--top">
  <div class="photo" style="left:0;top:0;width:250px;height:46px" role="img" aria-label="Photo of sandwiches on a board"></div>
  <div class="photo" style="left:550px;top:0;width:250px;height:46px" role="img" aria-label="Photo of fresh salads"></div>
  <div class="tab script" style="left:258px;top:0;width:284px;height:40px">Sandwiches</div>

  <div class="sheet" style="left:10px;top:46px;width:780px;height:542px"></div>

  <!-- Sandwiches column -->
  <div class="head-tag" style="left:20px;top:52px">Sandwiches</div>
  <div class="item" style="left:22px;top:84px;width:226px"><b>Ham Reuben<span>$7.00</span></b>Shaved ham, sauerkraut, Swiss and dressing on toasted rye bread.</div>
  <div class="item" style="left:22px;top:144px;width:226px"><b>Traditional Turkey<span>$6.50</span></b>Roasted turkey, lettuce, tomato and mayo on your choice of bread.</div>
  <div class="item" style="left:22px;top:204px;width:226px"><b>Hot Rodea<span>$7.00</span></b>Pepper jack, sliced jalapeños and roast beef grilled until warm.</div>
  <div class="item" style="left:22px;top:264px;width:226px"><b>Cream Cheese Veggie Bagel<span>$5.50</span></b>Toasted bagel with herb cream cheese, cucumber and sprouts.</div>
  <div class="item" style="left:22px;top:324px;width:226px"><b>Roosevelt Roast Beef<span>$6.75</span></b>Thin sliced roast beef, cheddar and horseradish spread.</div>
  <div class="item" style="left:22px;top:384px;width:226px"><b>Eastern BLT<span>$6.00</span></b>Thick bacon, crisp lettuce and ripe tomato on sourdough.</div>
  <div class="item" style="left:22px;top:444px;width:226px"><b>Meatball Hoagie<span>$7.25</span></b>Meatballs in marinara with melted mozzarella on a hoagie roll.</div>
  <div class="item" style="left:22px;top:504px;width:226px"><b>Blackened Club<span>$7.50</span></b>Blackened chicken, bacon, ham, lettuce and tomato, triple stacked.</div>

  <!-- Middle column -->
  <div class="item" style="left:268px;top:56px;width:262px"><b>Pecan Chicken Salad Sandwich<span>$6.50</span></b>House chicken salad with pecans and grapes on a croissant.</div>
  <div class="item" style="left:268px;top:104px;width:262px"><b>Tuna Salad Sandwich<span>$6.00</span></b>Albacore tuna salad with celery, lettuce and tomato.</div>
  <div class="item" style="left:268px;top:152px;width:262px"><b>Chicken Bacon Ranch Hoagie<span>$7.00</span></b>Grilled chicken, bacon and ranch with melted cheddar.</div>
  <div class="item" style="left:268px;top:200px;width:262px"><b>Tex<span>$6.75</span></b>Smoked brisket, pickled onions and green chile on a bun.</div>
  <div class="item" style="left:268px;top:248px;width:262px"><b>Italian Herb<span>$6.75</span></b>Salami, ham, provolone and herb vinaigrette on focaccia.</div>
  <div class="photo" style="left:268px;top:300px;width:84px;height:70px" role="img" aria-label="Photo of a club sandwich"></div>
  <div class="photo" style="left:357px;top:300px;width:84px;height:70px" role="img" aria-label="Photo of a hoagie"></div>
  <div class="photo" style="left:446px;top:300px;width:84px;height:70px" role="img" aria-label="Photo of a wrap cut in half"></div>
  <div class="wraps-band" style="left:268px;top:382px;width:262px">Wraps</div>
  <div class="price-badge" style="left:452px;top:370px;width:62px;height:62px;font-size:17px">$6.50</div>
  <div class="wrap-text" style="left:268px;top:420px;width:262px">
    Choose from the following:<br>
    <strong>TORTILLA</strong> – Tomato Basil, Jalapeño Cheddar, Garlic Herb<br>
    <strong>MEAT</strong> – Turkey, ham or roast beef<br>
    <strong>CHEESE</strong> – cheddar, pepper jack, Swiss or provolone<br>
    <strong>SAUCE</strong> – Mayo, Ranch, Honey Mustard, Mustard<br>
    <strong>VEGGIES</strong> – lettuce, tomato, onion, cucumber, spinach, olives
  </div>

  <!-- Salads column -->
  <div class="head-tag" style="left:688px;top:52px">Salads</div>
  <div class="item" style="left:552px;top:84px;width:228px"><b>Chef Salad<span>$6.50</span></b>Ham, turkey, egg and cheddar on mixed greens.</div>
  <div class="item" style="left:552px;top:128px;width:228px"><b>Grilled Chicken Salad<span>$6.75</span></b>Grilled chicken, tomato and croutons on romaine.</div>
  <div class="item" style="left:552px;top:172px;width:228px"><b>Pecan Chicken Salad<span>$6.50</span></b>Pecan chicken salad scooped over crisp greens.</div>
  <div class="item" style="left:552px;top:216px;width:228px"><b>Tuna Salad Salad<span>$6.00</span></b>Tuna salad with cucumber and tomato on greens.</div>
  <div class="item" style="left:552px;top:260px;width:228px"><b>Side Salad<span>$3.50</span></b>Small garden salad with your choice of dressing.</div>
  <div class="item" style="left:552px;top:304px;width:228px"><b>Guacamole &amp; Chips<span>$4.00</span></b>Fresh made guacamole with tortilla chips.</div>
  <div class="photo" style="left:552px;top:346px;width:120px;height:100px" role="img" aria-label="Photo of a fresh fruit cup"></div>
  <div class="fruit-tag" style="left:680px;top:370px;width:100px">Fresh Fruit Cup<br><span style="font-family:'Roboto Condensed',sans-serif;font-size:10px">$3.00</span></div>
  <div class="extras" style="left:552px;top:456px;width:228px">
    <h4>Extras</h4>
    Gluten free bread $.50 · Cheese $.50<br>
    Meat $1.00 · Bacon $1.00<br>
    Avocado $.75 · Extra dressing $.25<br>
    Guacamole side $1.50
  </div>
</section>

<!-- BOTTOM PANEL -->
<section class="panel panel--bottom">
  <div class="photo" style="left:0;top:0;width:560px;height:48px" role="img" aria-label="Photo strip of pastries, soups and coffee"></div>
  <div class="sheet" style="left:10px;top:52px;width:560px;height:538px"></div>

  <!-- Sides -->
  <div class="head-tag" style="left:20px;top:58px">Sides</div>
  <table class="sides-table" style="left:18px;top:88px;width:220px">
    <tr><th></th><th>Small</th><th>Medium</th><th>Large</th></tr>
    <tr><td>Pasta Salad</td><td>$1.50</td><td>$2.50</td><td>$3.50</td></tr>
    <tr><td>Coleslaw</td><td>$1.50</td><td>$2.50</td><td>$3.50</td></tr>
    <tr><td>Potato Salad</td><td>$1.50</td><td>$2.50</td><td>$3.50</td></tr>
  </table>
  <div class="pastry" style="top:160px"><div class="photo photo--round" role="img" aria-label="Photo of a cookie"></div><div class="item"><b>Single Cookie<span>$1.00</span></b>Baked fresh daily in house.</div></div>
  <div class="pastry" style="top:212px"><div class="photo photo--round" role="img" aria-label="Photo of a slice of cake"></div><div class="item"><b>Slice of Cake<span>$2.50</span></b>Ask for today's cake flavor.</div></div>
  <div class="pastry" style="top:264px"><div class="photo photo--round" role="img" aria-label="Photo of a slice of pie"></div><div class="item"><b>Slice of Pie<span>$2.75</span></b>Seasonal fruit and cream pies.</div></div>
  <div class="pastry" style="top:316px"><div class="photo photo--round" role="img" aria-label="Photo of a brownie"></div><div class="item"><b>Brownie<span>$1.75</span></b>Rich fudge brownie with walnuts.</div></div>
  <div class="pastry" style="top:368px"><div class="photo photo--round" role="img" aria-label="Photo of a cinnamon roll"></div><div class="item"><b>Cinnamon Roll<span>$2.50</span></b>Warm roll with cream cheese icing.</div></div>
  <div class="pastry" style="top:420px"><div class="photo photo--round" role="img" aria-label="Photo of an apple fritter"></div><div class="item"><b>Apple Fritter<span>$2.25</span></b>Glazed fritter with apple pieces.</div></div>
  <div class="pastry" style="top:472px"><div class="photo photo--round" role="img" aria-label="Photo of a cupcake"></div><div class="item"><b>Cupcake<span>$2.00</span></b>Frosted cupcake, flavors vary.</div></div>
  <div class="pastry" style="top:524px"><div class="photo photo--round" role="img" aria-label="Photo of a scone"></div><div class="item"><b>Scone<span>$2.25</span></b>Buttery scone baked each morning.</div></div>

  <!-- Soups / Kids / Desserts -->
  <div class="head-tag" style="left:262px;top:58px">Soups</div>
  <div class="item" style="left:262px;top:90px;width:296px;font-size:11px">Available in 3 sizes<br>Ask your server for daily soup options</div>
  <div class="size-bar" style="left:262px;top:122px;width:296px;height:26px"><span>SM 2.99</span><span>LG 3.99</span><span>FAMILY 12.99</span></div>
  <div class="kids-pill" style="left:262px;top:160px">Kids Menu</div>
  <div class="kid-box" style="left:262px;top:190px;width:142px;height:86px"><b>Little Rascal PB&amp;J</b>Peanut butter and jelly with chips and a juice box<i>$4.50</i></div>
  <div class="kid-box" style="left:416px;top:190px;width:142px;height:86px"><b>Grownup Grilled Cheese</b>Melted cheddar on white bread with chips<i>$4.50</i></div>
  <div class="script" style="position:absolute;left:360px;top:286px;font-size:24px">Desserts</div>
  <div class="photo photo--round" style="left:262px;top:324px;width:48px;height:48px" role="img" aria-label="Photo of muffins"></div>
  <div class="item" style="left:318px;top:326px;width:240px"><b>Muffins<span>$1.75</span></b>Blueberry, banana nut or chocolate chip, baked fresh.</div>
  <div class="photo photo--round" style="left:262px;top:380px;width:48px;height:48px" role="img" aria-label="Photo of bagels"></div>
  <div class="item" style="left:318px;top:382px;width:240px"><b>Bagels<span>$1.50</span></b>Plain, everything or cinnamon raisin with cream cheese.</div>
  <div class="photo photo--round" style="left:262px;top:436px;width:48px;height:48px" role="img" aria-label="Photo of cookies with milk"></div>
  <div class="item" style="left:318px;top:438px;width:240px"><b>2 Fresh Cookies w/ Milk<span>$2.50</span></b>Two warm cookies served with a cold glass of milk.</div>
  <div class="note" style="left:262px;top:494px;width:296px">THESE ITEMS CAN BE MADE IN-HOUSE OR ORDERED AHEAD. PRICES MAY VARY WITH THE SEASON. PLEASE ASK US ABOUT CATERING.</div>
  <div class="thanks" style="left:262px;top:552px;width:296px">Thank you for visiting Pebble Brook Cafe,<br>we truly appreciate your business.</div>

  <!-- Brand card -->
  <div class="brand-card" style="left:582px;top:10px;width:206px;height:578px">
    <div class="ribbon">Pebble Brook Cafe</div>
    <div class="photo" style="left:16px;top:80px;width:174px;height:150px" role="img" aria-label="Photo of a coffee cup and pastries"></div>
    <div class="icons">
      <div><svg width="26" height="26" viewBox="0 0 26 26"><circle cx="13" cy="13" r="12" fill="none" stroke="#9a2f17" stroke-width="1.5"/><path d="M8 9h9v6a4 4 0 0 1-4 4h-1a4 4 0 0 1-4-4z" fill="#9a2f17"/></svg>Drinks</div>
      <div><svg width="26" height="26" viewBox="0 0 26 26"><circle cx="13" cy="13" r="12" fill="none" stroke="#9a2f17" stroke-width="1.5"/><path d="M7 14h12v2H7zM8 11h10v2H8z" fill="#9a2f17"/></svg>Foods</div>
      <div><svg width="26" height="26" viewBox="0 0 26 26"><circle cx="13" cy="13" r="12" fill="none" stroke="#9a2f17" stroke-width="1.5"/><path d="M9 13h8l-4 7z" fill="#9a2f17"/><circle cx="13" cy="11" r="3" fill="#9a2f17"/></svg>Desserts</div>
    </div>
    <div class="menu-rule"></div>
    <div class="menu-word">MENU</div>
    <div class="menu-rule menu-rule--low"></div>
    <div class="photo" style="left:16px;top:380px;width:174px;height:180px" role="img" aria-label="Photo of a coffee shop counter"></div>
  </div>
</section>

</body>
</html>
```